Website homepage rework for women's travel website

I have a homepage (http://www.ladies-far-afield.example) that I'm 50% happy with but don't want to completely overhaul. I'd like to retain a similar look but upgrade it to something a bit more modern and less old-fashioned. The basic sense of the site is empowering, self-confident, fun and adventurous - but female and over 40.

A number of the elements on the page have to be redesigned, a few can be tweaked, and a few left alone. See the rest of the brief for further information.

Target Market(s)

women over 40 who like to travel

Industry/Entity Type

Travel

Number of Pages Required

1 page

Font styles to use
Other font styles liked:
• see my brief

Requirements
Must have
• - size - the page must be significantly wider
• - the only font I MUST keep is Raleway (as in the tagline) and possibly the font of the site name (Ladies Far Afield). Both of those work for me. There are too many fonts on the page, however, and that needs to be unified.
• - the rectangles I click to get inside the site have to change to something more modern, possibly square - they do not have to be separated into two columns as they are now, nor do they need the titles (toolkit etc)
• - I like the background image of the header - but it needs to be wider of course - also keep in mind the aspect - it has to fit into the smaller inside pages, whose size will not change
• - at the end of the project I need to receive the separate elements of the design so I can eventually make a change myself if needed ie. replace my own photo, for example
Nice to have
• - the three photos need to change to something more eye-popping - or something else should take their place to fill the space
Should not have
• I do not want a full, original redesign. I want my readers to still feel as though they are on the same site - same header, mostly same fonts.

```html
<!DOCTYPE html>
<html lang="en">
<head>
<meta charset="utf-8">
<title>Ladies Far Afield</title>
<link rel="stylesheet" href="https://fonts.googleapis.com/css2?family=Oswald:wght@300;400&family=Raleway:wght@400;600;700&display=swap">
<style>
:root{
  --ink:#2b2826;
  --paper:#f1f0eb;
  --orange:#ec8a13;
  --text:#3a3633;
  --light:#f4efe6;
  --card:#ffffff;
}
*{margin:0;padding:0;box-sizing:border-box}
html,body{width:1200px;height:1200px;overflow:hidden}
body{position:relative;background:var(--paper);font-family:'Raleway',sans-serif;color:var(--text)}
.nav{position:absolute;top:0;left:0;width:1200px;height:48px;background:var(--ink)}
.nav a{position:absolute;top:10px;font-family:'Oswald',sans-serif;font-weight:300;font-size:21px;color:var(--light);text-decoration:none;line-height:26px}
.nav a.is-active{color:var(--orange)}
.nav a.is-active::after{content:"";position:absolute;left:0;right:0;top:36px;height:2px;background:var(--orange)}
.hero{position:absolute;top:48px;left:0;width:1200px;height:234px;background:radial-gradient(ellipse at 70% 30%,#d8a25c 0%,#a8692c 35%,#5a3716 75%,#2e1d0e 100%)}
.hero-photo{position:absolute;top:30px;left:300px;width:200px;height:170px;background:linear-gradient(#8d7a64,#4e4031);border-radius:6px;opacity:.55}
.hero-title{position:absolute;top:72px;left:560px;width:356px;text-align:center;font-family:'Oswald',sans-serif;color:#fff;text-shadow:0 2px 6px rgba(0,0,0,.35)}
.hero-title h1{font-weight:400;font-size:48px;line-height:56px}
.hero-title p{font-weight:300;font-size:19px;line-height:22px}
.intro{position:absolute;top:282px;left:0;width:1200px;height:200px}
.intro-lead{position:absolute;left:204px;top:32px;font-size:16px}
.intro-lead strong{color:var(--orange);font-weight:600}
.intro ul{position:absolute;left:228px;top:66px;list-style:none}
.intro li{font-size:16px;line-height:37px;position:relative;padding-left:24px}
.intro li::before{content:"•";position:absolute;left:0;font-size:10px}
.intro li b{font-weight:700;color:#1e1b19}
.portrait{position:absolute;left:814px;top:18px;width:164px;height:164px;border-radius:50%;border:4px solid #fff;box-shadow:0 0 0 1px #d6d3cc;background:radial-gradient(circle at 50% 40%,#a89a8c,#2b2826 70%)}
.cta{position:absolute;top:482px;left:0;width:1200px;height:47px;background:var(--ink);font-family:'Oswald',sans-serif;font-weight:300;font-size:24px;color:var(--light)}
.cta span{position:absolute;top:8px;line-height:30px}
.cta em{font-style:normal;color:var(--orange)}
.cta-button{position:absolute;left:580px;top:7px;width:116px;height:33px;background:var(--orange);border-radius:2px;color:#fff;font-weight:400;text-align:center;line-height:34px;letter-spacing:.5px}
.section-title{position:absolute;left:198px;width:804px;height:30px;display:flex;align-items:center;gap:16px;font-weight:700;font-size:22px;color:#2b2826}
.section-title::before,.section-title::after{content:"";flex:1;height:2px;background:var(--orange)}
.tile{position:absolute;width:167px;height:201px;background:var(--card);clip-path:polygon(0 0,100% 0,100% 88%,50% 100%,0 88%);filter:drop-shadow(0 0 1px #ddd)}
.tile .thumb{position:absolute;left:4px;top:4px;width:159px;height:159px;display:flex;align-items:center;justify-content:center}
.tile .label{position:absolute;top:169px;left:0;width:100%;text-align:center;font-size:13px;color:#333}
.thumb-overlay{background:linear-gradient(#d98a1f,#c9781a);font-family:'Oswald',sans-serif;font-size:11px;color:#fff}
.footer{position:absolute;top:1160px;left:0;width:1200px;height:40px;background:var(--ink);text-align:center;font-family:'Oswald',sans-serif;font-size:11px;color:var(--light);line-height:40px}
</style>
</head>
<body>
<nav class="nav">
  <a class="is-active" style="left:204px">START HERE</a>
  <a style="left:352px">ABOUT</a>
  <a style="left:466px">TRAVEL RESOURCES</a>
  <a style="left:669px">BLOG</a>
  <a style="left:774px">TRAVEL SHOP</a>
  <a style="left:933px">CONTACT</a>
</nav>

<header class="hero" role="img" aria-label="Camper van driving across a dusty golden plain">
  <div class="hero-photo"></div>
  <div class="hero-title">
    <h1>Ladies Far Afield</h1>
    <p>For women who travel smart, safe + solo</p>
  </div>
</header>

<section class="intro">
  <p class="intro-lead">Hi, I'm <strong>Mara</strong>. I took my first solo trip at 15. I'll show you how to travel...</p>
  <ul>
    <li><b>Smart:</b> practical tools to help you plan – and afford – the perfect trip</li>
    <li><b>Safe:</b> down-to-earth advice and a ton of safety recommendations</li>
    <li><b>Solo:</b> yes, you can do it!</li>
  </ul>
  <div class="portrait" role="img" aria-label="Portrait photo of the site author"></div>
</section>

<section class="cta">
  <span style="left:353px">Thinking of <em>solo</em> travel?</span>
  <span class="cta-button">CLICK HERE</span>
  <span style="left:712px">to find out <em>how</em></span>
</section>

<h2 class="section-title" style="top:559px">Destinations</h2>
<a class="tile" style="left:198px;top:627px"><div class="thumb thumb-overlay" role="img" aria-label="Lake and forested hills, tinted orange">Does it really take two to tango?</div><div class="label">Solo in Argentina</div></a>
<a class="tile" style="left:410px;top:627px"><div class="thumb" role="img" aria-label="Custard tart on a plate" style="background:radial-gradient(circle at 50% 45%,#d9a24a,#9a8a78 60%,#6f6a66)"></div><div class="label">Europe for foodies</div></a>
<a class="tile" style="left:623px;top:627px"><div class="thumb" role="img" aria-label="Yurts by a lake under a cloudy sky" style="background:linear-gradient(#9fb6cc 0%,#c9c3b0 45%,#6a6a5c 60%,#3f3d33 100%)"></div><div class="label">Solo female travel</div></a>
<a class="tile" style="left:836px;top:627px"><div class="thumb" role="img" aria-label="Street book stall with stacks of books and flowers" style="background:linear-gradient(#8a8f96,#5c5a52 50%,#2f2c27)"></div><div class="label">Rebellious carouge</div></a>

<h2 class="section-title" style="top:857px">Travel Toolkit</h2>
<a class="tile" style="left:198px;top:924px"><div class="thumb" role="img" aria-label="Shared table with plates of food" style="background:linear-gradient(#6a4a34,#b89070 50%,#3e5a4e)"></div><div class="label">Eating with locals</div></a>
<a class="tile" style="left:410px;top:924px"><div class="thumb" role="img" aria-label="Travel gear laid out for packing" style="background:linear-gradient(#6a5a4e,#3b3a48 55%,#2a2f5a)"></div><div class="label">Your packing list</div></a>
<a class="tile" style="left:623px;top:924px"><div class="thumb" role="img" aria-label="Cruise ship lit blue at night" style="background:radial-gradient(circle at 50% 50%,#2f5fd8,#0c1230 65%,#05070f)"></div><div class="label">No single supplement</div></a>
<a class="tile" style="left:836px;top:924px"><div class="thumb" role="img" aria-label="Aircraft wing above the clouds" style="background:linear-gradient(160deg,#1c3f7a,#6a8ab8 45%,#c9d0d8 80%)"></div><div class="label">Stress management course</div></a>

<footer class="footer">Copyright @ 2016 www.ladies-far-afield.example</footer>
</body>
</html>
```